School website design - Technology and the arts

We will need a new or updated design that incorporates the following features:
-Reactive design that changes with the needs of the device.
-Static Background - only content scrolls
-Static Menu - similar to the Pressly Harbor Lantern theme
-Alert box for important notices (closings/emergency use only) that doesn’t display unless active
-Margins must be wider than “standard pressly theme” (fits the entire display at any resolution, doesn’t just center a columned design)
-Features an image scroll on the front page to show our current works/progress. (only if the screen is big enough). Should have swipe capability
-We must have a place on the front page to display the current school news as well as a location to display current events with a poster (see current webdesign for example)
-Uses the school colors (green and gold/yellow) in a way that is pleasing to the eye.
-Unique design to our school that is very clean and modern.
-Events need to be able to pop-out when you mouseover in a desktop environment. Example: http://skinvault.example/category/pressly/creative (mouse over a theme and it shows additional information about it without a refresh)
-Custom Admin panel to easily updated the news and events section.
-Notes: We are currently using some free icons that we found to make the current site look not so boring since we do not have a lot of content on each page. We would like to step away from that and are open to suggestions. Possibly something like http://vormlab.example/demo/?theme=arch under the services section but smaller.
-Notes 2: We have plenty of pictures of our building and activities that can be used as a background, etc.
-We are open to new ideas and suggestions.

Our current website is https://www.kelmont-academy.example to get an idea on how we manage our current site.

```html
<!DOCTYPE html>
<html lang="en">
<head>
<meta charset="utf-8">
<title>Kelmont Regional Academy</title>
<link rel="stylesheet" href="https://fonts.googleapis.com/css2?family=Open+Sans:ital,wght@0,400;0,600;0,700;1,400&family=PT+Sans+Narrow:wght@400;700&display=swap">
<style>
:root{
  --green-dark:#0b3a05;
  --green-text:#1d4a12;
  --gold:#f4c200;
  --ink:#1a1a1a;
  --muted:#555;
  --rule:#333;
  --white:#ffffff;
}
*{margin:0;padding:0;box-sizing:border-box}
html,body{width:1200px;height:955px;overflow:hidden}
body{position:relative;background:var(--white);font-family:"Open Sans",sans-serif;color:var(--ink)}
a{color:inherit;text-decoration:none}
.campus-backdrop{position:absolute;left:0;top:232px;width:1200px;height:723px;
  background:linear-gradient(180deg,#7d8478 0%,#8f9788 30%,#a7ad9c 55%,#6f8a3f 80%,#5f7b33 100%)}
.brand{position:absolute;left:84px;top:30px;width:110px;display:flex;flex-direction:column;align-items:center;gap:6px}
.brand-mark{width:46px;height:46px;border-radius:50%;background:var(--green-dark)}
.brand-name{font-family:"PT Sans Narrow",sans-serif;font-weight:700;font-size:14px;line-height:1.1;color:var(--green-dark);text-align:center}
.utility{position:absolute;right:84px;top:16px;font-family:"PT Sans Narrow",sans-serif;font-size:12px;color:#444;display:flex;gap:8px}
.utility span.sep{color:#444}
.search{position:absolute;left:883px;top:40px;width:233px;height:28px;border:1px solid #555;background:#fff}
.search svg{position:absolute;right:8px;top:6px}
.main-nav{position:absolute;right:84px;top:83px;display:flex;gap:27px;font-family:"PT Sans Narrow",sans-serif;font-weight:700;font-size:16px;color:#111}
.content-panel{position:absolute;left:66px;top:122px;width:798px;height:833px;background:rgba(255,255,255,.86);box-shadow:0 0 6px rgba(0,0,0,.35)}
.hero{position:absolute;left:84px;top:141px;width:762px;height:356px;
  background:radial-gradient(ellipse at 50% 60%,#e0902a 0%,#b85a18 30%,#4a3a9a 70%,#33287a 100%)}
.hero-caption{position:absolute;left:0;right:0;bottom:0;height:60px;background:linear-gradient(180deg,rgba(0,0,0,0),rgba(0,0,0,.45));
  color:#fff;font-size:23px;text-align:center;line-height:1;padding-top:24px}
.section-head{position:absolute;top:533px;height:30px;border-bottom:1px solid var(--rule);display:flex;align-items:center;gap:6px;padding-left:10px}
.section-head h2{font-size:16px;font-weight:700;letter-spacing:.2px}
.section-head .notch{position:absolute;left:18px;bottom:-9px}
.news{left:84px;width:362px}
.events{left:484px;width:362px}
.news-item{position:absolute;left:84px;width:362px;height:106px;border-bottom:1px solid #999}
.news-thumb{position:absolute;left:1px;top:0;width:75px;height:75px}
.news-body{position:absolute;left:86px;top:0;width:276px}
.news-date{font-size:9px;font-style:italic;color:#444;line-height:12px}
.news-title{display:inline-block;font-family:"PT Sans Narrow",sans-serif;font-weight:700;font-size:15px;color:var(--green-text);border-bottom:1px solid var(--green-text);line-height:17px;margin-top:2px}
.news-text{font-size:12.5px;line-height:16px;color:#222;margin-top:4px;white-space:nowrap;overflow:hidden;text-overflow:ellipsis}
.more-link{position:absolute;font-size:10.5px;font-weight:700;font-style:italic;color:var(--gold);text-decoration:underline}
.poster{position:absolute;left:485px;top:590px;width:360px;height:237px;background:linear-gradient(180deg,#8fbce8 0%,#7fb2e2 60%,#2a2a2a 100%)}
.event-title{position:absolute;left:484px;width:362px;top:834px;text-align:center;font-family:"PT Sans Narrow",sans-serif;font-weight:700;font-size:15px;color:var(--green-text)}
.event-title span{border-bottom:1px solid var(--green-text)}
.event-date{position:absolute;left:484px;width:362px;top:858px;text-align:center;font-size:12.5px;font-style:italic}
.event-rule{position:absolute;left:484px;width:362px;top:888px;border-top:1px solid #999}
.sidebar{position:absolute;left:864px;top:158px;width:270px;height:779px;background:var(--green-dark);color:#fff}
.sidebar .inner{position:absolute;left:19px;width:233px}
.mission h2{font-size:19px;font-weight:700;letter-spacing:.3px}
.mission p{font-size:12.6px;line-height:19.7px;margin-top:6px}
.sidebar .more-link{right:0}
.side-head{border-top:1px solid #fff;border-bottom:1px solid #fff;font-size:12.5px;font-weight:700;padding:6px 0 7px}
.study-cols{display:flex;gap:0;margin-top:15px}
.study-cols div{width:116px}
.study-cols h3{font-size:12.6px;font-weight:600;line-height:19.7px}
.study-cols ul{list-style:none}
.study-cols li{font-size:12.6px;line-height:19.7px;color:var(--gold)}
.study-cols li::before{content:"•";color:#fff;margin-right:7px;font-size:10px}
.address{font-size:12.6px;line-height:19.7px}
.social{display:flex;gap:5px;margin-top:5px}
.social span{width:15px;height:15px;background:#3a6fb5;border:1px solid #fff}
.copyright{position:absolute;right:18px;top:736px;font-size:9.5px;font-style:italic;color:#ddd}
</style>
</head>
<body>
<div class="campus-backdrop" role="img" aria-label="Campus building with trees and lawn in the background"></div>

<header>
  <a class="brand" href="#"><span class="brand-mark"></span><span class="brand-name">Kelmont Regional Academy</span></a>
  <nav class="utility"><a href="#">KRA EMAIL</a><span class="sep">|</span><a href="#">CALENDARS</a><span class="sep">|</span><a href="#">CONTACT US</a></nav>
  <div class="search"><svg width="17" height="17" viewBox="0 0 17 17"><circle cx="7" cy="7" r="5.5" fill="none" stroke="#888" stroke-width="2"/><line x1="11" y1="11" x2="16" y2="16" stroke="#888" stroke-width="2.5"/></svg></div>
  <nav class="main-nav"><a href="#">ABOUT KRA</a><a href="#">STUDENTS/PARENTS</a><a href="#">FACULTY/STAFF</a><a href="#">DOCUMENTS/FORMS</a><a href="#">PROGRAMS OF STUDY</a><a href="#">SERVICES</a><a href="#">QUICK LINKS</a></nav>
</header>

<main class="content-panel"></main>

<section class="hero" role="img" aria-label="Dancers in orange costumes performing on stage under purple light">
  <div class="hero-caption">Headline Goes Here</div>
</section>

<div class="section-head news">
  <svg width="24" height="20" viewBox="0 0 24 20"><rect x="1" y="1" width="22" height="18" fill="none" stroke="#111" stroke-width="2"/><rect x="4" y="4" width="7" height="6" fill="#111"/><line x1="13" y1="5" x2="20" y2="5" stroke="#111" stroke-width="2"/><line x1="13" y1="9" x2="20" y2="9" stroke="#111" stroke-width="2"/><line x1="4" y1="14" x2="20" y2="14" stroke="#111" stroke-width="2"/></svg>
  <h2>RECENT NEWS</h2>
  <svg class="notch" width="18" height="9" viewBox="0 0 18 9"><polygon points="0,0 18,0 9,8" fill="#fff" stroke="#333"/><line x1="0" y1="0" x2="18" y2="0" stroke="#fff" stroke-width="2"/></svg>
</div>
<div class="section-head events">
  <svg width="20" height="20" viewBox="0 0 20 20"><rect x="1" y="3" width="18" height="16" fill="none" stroke="#111" stroke-width="2"/><rect x="1" y="3" width="18" height="4" fill="#111"/><g fill="#111"><rect x="4" y="9" width="3" height="3"/><rect x="9" y="9" width="3" height="3"/><rect x="14" y="9" width="3" height="3"/><rect x="4" y="14" width="3" height="3"/><rect x="9" y="14" width="3" height="3"/></g></svg>
  <h2>UPCOMING EVENT</h2>
  <svg class="notch" width="18" height="9" viewBox="0 0 18 9"><polygon points="0,0 18,0 9,8" fill="#fff" stroke="#333"/><line x1="0" y1="0" x2="18" y2="0" stroke="#fff" stroke-width="2"/></svg>
</div>

<article class="news-item" style="top:590px">
  <div class="news-thumb" role="img" aria-label="Students in costume on stage" style="background:linear-gradient(135deg,#a57a4a,#5a3a2a)"></div>
  <div class="news-body"><p class="news-date">April 1, 2014</p><a class="news-title" href="#">Lorem Ipsum Dolor Sit Amet Consectetur</a><p class="news-text">Lorem ipsum dolor sit amet, consectetur</p><p class="news-text" style="margin-top:0">adipiscing elit. Mauris eget elementum magna…</p></div>
</article>
<article class="news-item" style="top:696px">
  <div class="news-thumb" role="img" aria-label="Students in dark uniforms performing" style="background:linear-gradient(135deg,#4a4a44,#1e221c)"></div>
  <div class="news-body"><p class="news-date">March 30, 2014</p><a class="news-title" href="#">Quisque At Lacus Nulla Curabitur Orci Dui</a><p class="news-text">Quisque at lacus nulla. Curabitur orci dui, lao</p><p class="news-text" style="margin-top:0">reet a mollis at, hendrerit nec enim uspendis…</p></div>
</article>
<article class="news-item" style="top:802px">
  <div class="news-thumb" role="img" aria-label="Student playing the piano" style="background:linear-gradient(135deg,#8a6a4a,#2a1e16)"></div>
  <div class="news-body"><p class="news-date">March 27, 2014</p><a class="news-title" href="#">Donec Urna Turpis Euismod Rna Ornare Interdum</a><p class="news-text">Donec urna turpis, euismod eu urna ornare,</p><p class="news-text" style="margin-top:0">interdum vestibulum nibh. Donec sagittis…</p></div>
</article>
<a class="more-link" href="#" style="right:754px;top:903px">VIEW ALL NEWS &gt;</a>

<div class="poster" role="img" aria-label="Event poster for the student production As You Like It"></div>
<p class="event-title"><span>As You Like It</span></p>
<p class="event-date">March 16 @ 2:00 pm</p>
<div class="event-rule"></div>
<a class="more-link" href="#" style="right:354px;top:899px">VIEW ALL EVENTS &gt;</a>

<aside class="sidebar">
  <div class="inner mission" style="top:44px">
    <h2>OUR MISSION</h2>
    <p>The Kelmont Regional Academy for the Arts and Technology provides gifted and talented students a differentiated and rigorous education, cultivates a supportive environment that inspires unique artistic and technological visions, promotes cultural tolerance, nurtures community partnerships, and produces active, engaged citizens.</p>
  </div>
  <a class="more-link" href="#" style="right:19px;top:253px">LEARN MORE &gt;</a>

  <div class="inner" style="top:322px">
    <h3 class="side-head">PROGRAMS OF STUDY</h3>
    <div class="study-cols">
      <div><h3>Focus Areas</h3><ul><li>Dance</li><li>Literary Arts</li><li>Music</li><li>Technology</li><li>Theatre Arts</li><li>Visual Arts</li></ul></div>
      <div><h3>Study Programs</h3><ul><li>English</li><li>Health and PE</li><li>Math</li><li>Science</li><li>Social Sciences</li><li>World Languages</li></ul></div>
    </div>
  </div>

  <div class="inner" style="top:556px">
    <h3 class="side-head" style="border-top-color:#fff">Location</h3>
    <p class="address" style="margin-top:15px">418 East Harlow Street<br>Brenton, VA 23890, United States<br>+1 555-014-0200</p>
    <div class="social"><span></span><span></span><span></span><span></span><span></span><span></span></div>
  </div>
  <p class="copyright">©2014 Kelmont Regional Academy.</p>
</aside>
</body>
</html>
```